Vantrell Law Letterhead

We need a new letterhead design for a Law Firm. The address for the law firm is 4817 Larkspur Boulevard, Suite 250, Houston, Texas 77342. Phone Number: 832-619-3057; Fax Number: 832-407-1694. The logo is uploaded to the project.

```html
<!DOCTYPE html>
<html lang="en">
<head>
<meta charset="utf-8">
<title>Vantrell Law Letterhead</title>
<link rel="stylesheet" href="https://fonts.googleapis.com/css2?family=Montserrat:wght@400;600&display=swap">
<style>
  :root {
    --backdrop: #e8e8e8;
    --paper: #ffffff;
    --navy: #1b2f5e;
    --red: #e0161e;
    --ink: #1e1e1e;
    --signature-tone: #ececec;
  }
  * { box-sizing: border-box; margin: 0; padding: 0; }
  html, body {
    width: 1154px; height: 1200px; overflow: hidden;
    background: var(--backdrop);
    font-family: "Montserrat", Arial, sans-serif;
    color: var(--ink);
  }
  .letterhead {
    position: absolute; left: 167px; top: 27px;
    width: 820px; height: 1146px;
    background: var(--paper);
    overflow: hidden;
  }
  .brand {
    position: absolute; left: 28px; top: 80px;
    display: flex; align-items: center; gap: 12px;
  }
  .brand-mark { width: 32px; height: 32px; background: var(--navy); }
  .brand-name {
    font-size: 29px; font-weight: 600; color: var(--navy);
  }
  .contact {
    position: absolute; left: 613px; top: 62px;
    border-left: 1.5px solid var(--red);
    padding-left: 12px;
    font-size: 13.5px; line-height: 17.6px;
    font-style: normal;
  }
  .contact-address { margin-bottom: 10px; }
  .contact-line { display: flex; align-items: center; gap: 8px; line-height: 20.5px; }
  .contact-line svg { width: 13px; height: 13px; fill: var(--red); }
  .header-rule {
    position: absolute; left: 29px; top: 195px;
    width: 760px; height: 2px; background: var(--red);
  }
  .recipient {
    position: absolute; left: 31px; top: 262px;
    font-size: 13px; line-height: 20.4px;
  }
  .letter-body {
    position: absolute; left: 32px; top: 347px; width: 760px;
    font-size: 13px; line-height: 20.4px;
    text-align: justify;
  }
  .letter-body p { margin-bottom: 20.4px; }
  .closing {
    position: absolute; left: 30px; top: 924px;
    font-size: 16px;
  }
  .signature {
    position: absolute; left: 29px; top: 955px;
    width: 92px; height: 30px;
    background: var(--signature-tone);
  }
  .footer-band {
    position: absolute; left: 0; top: 1000px;
    width: 820px; height: 146px;
    background: linear-gradient(180deg, var(--red) 0%, #8a1a2e 45%, var(--navy) 100%);
  }
</style>
</head>
<body>
  <main class="letterhead">
    <header>
      <div class="brand">
        <span class="brand-mark"></span>
        <span class="brand-name">Vantrell Law</span>
      </div>
      <address class="contact">
        <div class="contact-address">4817 Larkspur Boulevard,<br>Suite 250, Houston,<br>Texas 77342</div>
        <div class="contact-line">
          <svg viewBox="0 0 24 24" aria-hidden="true"><path d="M6.6 10.8a15.1 15.1 0 0 0 6.6 6.6l2.2-2.2a1 1 0 0 1 1-.25 11.4 11.4 0 0 0 3.6.57 1 1 0 0 1 1 1V20a1 1 0 0 1-1 1A17 17 0 0 1 3 4a1 1 0 0 1 1-1h3.5a1 1 0 0 1 1 1c0 1.25.2 2.45.57 3.57a1 1 0 0 1-.25 1z"/></svg>
          <span>832-619-3057</span>
        </div>
        <div class="contact-line">
          <svg viewBox="0 0 24 24" aria-hidden="true"><path d="M7 3h10v5H7zM4 9h16a2 2 0 0 1 2 2v6h-4v4H6v-4H2v-6a2 2 0 0 1 2-2zm4 7v3h8v-3z"/></svg>
          <span>832-407-1694</span>
        </div>
      </address>
      <div class="header-rule"></div>
    </header>

    <section class="recipient">
      Mr/s<br>First Name and Last Name<br>Company Name<br>Address
    </section>

    <section class="letter-body">
      <p>Lorem ipsum dolor sit amet,consectetur adipiscing sed do eiusmod tempor incididunt laboreet dolore magna aliqua.Ut enim ad minim.veniam, quis nostrud exercitation ullamco laboris nisi ut aliquip exea commodo consequat.Lorem ipsum dolor sit amet,consectetur adipiscing sed do eiusmod tempor incididunt.labore et dolore magna aliqua. Ut enim</p>
      <p>Lorem ipsum dolor sit amet, consectetur adipiscing sed do eiusmod tempor incididunt labore et dolore magna aliqua. Ut enim ad minim veniam, quis nostrud exercitation ullamco laboris nisi ut aliquip exea commodo consequat.Duis aute irure dolor in reprehenderit in voluptate velit esse cillum irure dolor in reprehenderit in voluptate velit esse irure</p>
      <p>Lorem ipsum dolor sit amet, consectetur adipiscing sed do eiusmod tempor incididunt labore et dolore magna aliqua. consequat. Duis aute irure dolor in.reprehenderit in voluptate velit esse cillum dolore eu fugiat nulla pariatur. Excepteur sint occaecat cupidatat non proident, sunt in culpa qui officia deserunt mollit,</p>
      <p>Lorem ipsum dolor sit amet, consectetur adipiscing sed do eiusmod tempor incididunt labore et dolore magna aliqua. Ut enim Lorem ipsum dolor sit amet, consectetur adipiscing sed do eiusmod tempor incididunt labore et dolore magna aliqua. Ut enim Lorem ipsum aliqua.ipsum</p>
      <p>Lorem ipsum dolor sit amet, consectetur adipiscing sed do eiusmod tempor incididunt labore et dolore magna aliqua. Ut enim ad minim veniam, quis nostrud exercitation ullamco laboris nisi ut aliquip exea commodo consequat.Duis aute irure dolor in reprehenderit in voluptate velit esse cillum irure dolor in reprehenderit in voluptate velit esse irure</p>
      <p>Lorem ipsum dolor sit amet, consectetur adipiscing sed do eiusmod tempor incididunt labore et dolore magna aliqua. Ut enim ad minim veniam, quis nostrud exercitation ullamco laboris nisi ut aliquip exea commodo consequat.Duis aute irure dolor in reprehenderit in voluptate velit esse cillum irure dolor in reprehenderit in voluptate velit esse irure</p>
    </section>

    <div class="closing">Regards</div>
    <div class="signature" role="img" aria-label="Handwritten signature"></div>

    <div class="footer-band" role="img" aria-label="Decorative red and navy footer band"></div>
  </main>
</body>
</html>
```